Fence Flyer to Attract More Sales During Winter

We need a new flyer made that we can distribute to residential mailboxes. The flyer is to promote our Frostline Picket Days. We like simply designs, and we would like the flyer to showcase a lot of our fence photos. More of our photos are online at our website at www.getbramblerail.com - our new address needs to also be featured on the flyer - 436 Quillen rd, Monroe, NC 28117. I do want the words "FROSTLINE PICKET DAYS" to be dominate on the flyer with the description "Wood fences starting at $12/FT!" Please look through our Facebook page and our website to gather more photos or information. We are flexible on colors, nothing to fancy - simple flyer design please.

Target Market(s)

Residential homeowners that need a new fence to enclose their yard for safety, security or decorative

Industry/Entity Type

Residential Construction

Font styles to use
Sans Serif

Colors

Designer to choose colors to be used in the design.

Requirements
Must have
• Frostline Picket Days
• Contact information for the business
• "Come visit our outdoor showroom, open 24/7!"
Nice to have
• Photos of our fences - you can find more on our website at www.GetBrambleRail.com or Facebook.com/MeadowlarkRailGPV
Should not have
• Flashy designs

```html
<!DOCTYPE html>
<html lang="en">
<head>
<meta charset="utf-8">
<title>Frostline Picket Days – Bramble Rail Fence</title>
<link href="https://fonts.googleapis.com/css2?family=Fredoka:wght@600;700&family=Lobster&family=Courgette&family=Exo+2:wght@600;700&display=swap" rel="stylesheet">
<style>
  :root {
    --backdrop: #e6e8ea;
    --sky: #86d0cc;
    --sky-light: #b4e3df;
    --snow: #ffffff;
    --teal-ink: #177f95;
    --tag-red: #e0603f;
    --brown-ink: #4a3328;
    --brand-blue: #2f79c4;
    --hole-yellow: #f1e58a;
    --scene-top: #9ad8d3;
    --scene-bottom: #d9efec;
    --photo-grass: #9fae6c;
    --photo-wood: #d9c08a;
    --photo-sky: #a9c3d9;
    --photo-siding: #cdd2d4;
  }
  * { box-sizing: border-box; margin: 0; padding: 0; }
  html, body { width: 1200px; height: 800px; overflow: hidden; background: var(--backdrop); }

  .flyer {
    position: absolute; left: 332px; top: 20px;
    width: 536px; height: 760px;
    background: var(--sky);
    overflow: hidden;
    box-shadow: 0 4px 14px rgba(0,0,0,.15);
  }

  .headline-top {
    position: absolute; left: 0; width: 100%; top: 42px;
    text-align: center;
    font-family: "Fredoka", sans-serif; font-weight: 700;
    font-size: 62px; letter-spacing: 1px;
    color: var(--snow);
    text-shadow: 2px 3px 0 rgba(90,120,125,.35);
  }
  .headline-script {
    position: absolute; left: 0; width: 100%; top: 92px;
    text-align: center;
    font-family: "Lobster", cursive; font-size: 78px;
    color: var(--teal-ink); line-height: 1;
    z-index: 3;
  }
  .sale-tag {
    position: absolute; left: 150px; top: 168px;
    width: 240px; height: 120px;
    transform: rotate(-14deg);
    z-index: 2;
  }
  .sale-tag__word {
    position: absolute; left: 22px; top: 22px; width: 160px;
    text-align: center;
    font-family: "Fredoka", sans-serif; font-weight: 700;
    font-size: 62px; line-height: 1; color: var(--snow);
  }

  .winter-scene {
    position: absolute; left: 0; top: 262px; width: 100%; height: 160px;
    background: linear-gradient(var(--scene-top), var(--scene-bottom));
  }
  .ground { position: absolute; left: 0; top: 390px; width: 536px; height: 370px; }

  .offer-lead {
    position: absolute; left: 0; width: 100%; top: 422px;
    text-align: center;
    font-family: "Courgette", cursive; font-size: 28px;
    color: var(--brown-ink);
  }
  .price-banner {
    position: absolute; left: 190px; top: 462px; width: 156px; height: 40px;
  }
  .price-banner__text {
    position: absolute; left: 0; top: 0; width: 100%; line-height: 40px;
    text-align: center;
    font-family: "Courgette", cursive; font-size: 27px; color: var(--snow);
  }

  .info-row {
    position: absolute; left: 13px; top: 516px; width: 512px; height: 52px;
    display: flex; align-items: center;
  }
  .brand { display: flex; align-items: center; width: 170px; gap: 6px; }
  .brand__mark { width: 14px; height: 14px; background: var(--brown-ink); flex: none; }
  .brand__name {
    font-family: "Exo 2", sans-serif; font-weight: 700; font-size: 14px;
    color: var(--brand-blue); line-height: 1.1;
  }
  .brand__phone {
    font-family: "Exo 2", sans-serif; font-weight: 700; font-size: 13px;
    color: #111; line-height: 1.2;
  }
  .brand__motto {
    font-family: "Exo 2", sans-serif; font-weight: 600; font-size: 5px; color: #333;
  }
  .divider { width: 0; height: 42px; border-left: 2px dotted var(--brown-ink); margin: 0 10px; }
  .showroom {
    font-family: "Courgette", cursive; font-size: 15px;
    color: var(--brown-ink); line-height: 1.45; white-space: nowrap;
  }
  .hours {
    font-family: "Courgette", cursive; font-size: 21px;
    color: var(--tag-red); line-height: 1.2;
  }

  .gallery {
    position: absolute; left: 13px; top: 585px; width: 510px; height: 163px;
    display: flex; justify-content: space-between;
  }
  .gallery__photo { width: 162px; height: 163px; }
  .gallery__photo--yard { background: linear-gradient(var(--photo-grass) 0 35%, var(--photo-wood) 35% 90%, #8a6a4a); }
  .gallery__photo--house { background: linear-gradient(var(--photo-sky) 0 25%, var(--photo-wood) 25% 85%, #b8a27a); }
  .gallery__photo--side { background: linear-gradient(var(--photo-siding) 0 20%, var(--photo-wood) 20% 88%, #c9a98a); }
</style>
</head>
<body>
  <main class="flyer">
    <div class="headline-top">FROSTLINE</div>
    <div class="headline-script">picket</div>

    <div class="sale-tag">
      <svg width="240" height="120" viewBox="0 0 240 120">
        <path d="M4 8 H178 L226 60 L178 112 H4 Z" fill="var(--tag-red)"/>
        <path d="M11 15 H174 L216 60 L174 105 H11 Z" fill="none" stroke="var(--snow)" stroke-width="2" stroke-dasharray="6 4"/>
        <circle cx="190" cy="60" r="10" fill="none" stroke="var(--hole-yellow)" stroke-width="4"/>
        <path d="M194 56 C215 30 238 10 234 4" fill="none" stroke="#333" stroke-width="1.5"/>
      </svg>
      <div class="sale-tag__word">DAYS</div>
    </div>

    <div class="winter-scene" role="img" aria-label="Illustration of snowy trees, small houses and picket fences along a snowy hill"></div>

    <svg class="ground" viewBox="0 0 536 370" preserveAspectRatio="none">
      <path d="M0 36 C120 12 300 0 536 4 V370 H0 Z" fill="var(--snow)"/>
    </svg>

    <div class="offer-lead">Wood fences starting at</div>
    <div class="price-banner">
      <svg width="156" height="40" viewBox="0 0 156 40">
        <path d="M0 0 H156 L146 20 L156 40 H0 L10 20 Z" fill="var(--tag-red)"/>
      </svg>
      <div class="price-banner__text">$12/FT!</div>
    </div>

    <section class="info-row">
      <div class="brand">
        <div class="brand__mark"></div>
        <div>
          <div class="brand__name">Bramble Rail Fence</div>
          <div class="brand__phone">704-555-0142</div>
          <div class="brand__motto">"Because Good Fences Make Good Neighbors"</div>
        </div>
      </div>
      <div class="divider"></div>
      <div class="showroom">
        Come visit our outdoor showroom!<br>
        436 Quillen rd, Monroe, NC 28117
      </div>
      <div class="divider"></div>
      <div class="hours">Open<br>24/7</div>
    </section>

    <section class="gallery">
      <div class="gallery__photo gallery__photo--yard" role="img" aria-label="Photo of a new wood privacy fence and gate around a grassy yard"></div>
      <div class="gallery__photo gallery__photo--house" role="img" aria-label="Photo of a wood picket fence in front of a brick house"></div>
      <div class="gallery__photo gallery__photo--side" role="img" aria-label="Photo of a scalloped wood fence beside a house"></div>
    </section>
  </main>
</body>
</html>
```